creating a certificate for our flagship course

Hi,
We need a new certificate for our flagship course called Bright Harbour. We have been running this course for 25 years this year and want to get something special that represents that. We need our logos incorporated and we love to have a compass or Koru incorporated in the certificate. We like something different from your standard certificate, but not too crazy.

The text should say something along the lines of:
This certificate is awarded to ....
For successfully completing and contributing to the three day Bright Harbour programme.

signed:... date:...

to learn a bit more about this course and our company, please check our website. www.hollisvantreeve.co.nz

Thank you!

Target Market(s)

attendees who completed our 3 day programme.

Requirements
Must have
• Both our BH logo and our brand logo. a compass or a koru.
• a 25th year existence something on it.

```html
<!DOCTYPE html>
<html lang="en">
<head>
<meta charset="utf-8">
<title>Certificate of Completion – Bright Harbour</title>
<link rel="stylesheet" href="https://fonts.googleapis.com/css2?family=Source+Sans+3:ital,wght@0,400;0,600;0,700;1,400;1,600&family=Pinyon+Script&display=swap">
<style>
  :root {
    --stage: #0d0d0d;
    --paper: #ffffff;
    --green: #2a8a14;
    --green-deep: #3f9a26;
    --green-mid: #8cbf78;
    --green-pale: #c6dcc0;
    --green-faint: #d3ecd0;
    --green-badge: #8bc34a;
    --ink: #1c1c1c;
    --ink-soft: #555a5e;
    --brand-ink: #3a3a4c;
  }
  * { box-sizing: border-box; }
  html, body {
    margin: 0;
    width: 1200px;
    height: 940px;
    overflow: hidden;
    background: var(--stage);
    font-family: "Source Sans 3", "Myriad Pro", Arial, sans-serif;
  }
  .certificate {
    position: absolute;
    left: 123px;
    top: 148px;
    width: 954px;
    height: 737px;
    background: var(--paper);
    overflow: hidden;
  }
  .compass-decoration,
  .swoosh {
    position: absolute;
    inset: 0;
    width: 954px;
    height: 737px;
  }
  .title {
    position: absolute;
    left: 55px;
    top: 94px;
    margin: 0;
    color: var(--green);
    font-weight: 700;
    line-height: 1;
  }
  .title-main {
    display: block;
    font-size: 60px;
    letter-spacing: 0.3px;
  }
  .title-sub {
    display: block;
    font-size: 26px;
    margin-top: 4px;
    margin-left: 2px;
  }
  .brand {
    position: absolute;
    left: 583px;
    top: 82px;
    display: flex;
    align-items: center;
    gap: 12px;
  }
  .brand-square {
    width: 51px;
    height: 51px;
    background: var(--green-badge);
  }
  .brand-name {
    color: var(--brand-ink);
    font-weight: 400;
    line-height: 1.05;
    letter-spacing: 1.5px;
  }
  .brand-name span { display: block; font-size: 21px; }
  .brand-name .brand-suffix { font-size: 13px; letter-spacing: 0.3px; }
  .award {
    position: absolute;
    left: 115px;
    top: 267px;
    height: 190px;
    width: 520px;
    border-left: 3px solid var(--green);
    padding-left: 40px;
  }
  .award-lead {
    margin: 0;
    font-style: italic;
    font-size: 20px;
    color: var(--ink);
  }
  .recipient {
    margin: 38px 0 0 3px;
    font-size: 33px;
    font-weight: 700;
    color: var(--green);
    letter-spacing: 0.3px;
  }
  .award-reason {
    margin: 28px 0 0 3px;
    font-style: italic;
    font-size: 16px;
    line-height: 22px;
    color: var(--ink);
  }
  .sign-field {
    position: absolute;
    top: 570px;
    width: 140px;
    border-top: 2px solid var(--green);
    text-align: center;
    font-style: italic;
    font-weight: 600;
    font-size: 14px;
    color: var(--ink);
    padding-top: 4px;
  }
  .sign-date { left: 163px; }
  .sign-signature { left: 452px; }
  .anniversary {
    position: absolute;
    left: 58px;
    top: 640px;
    margin: 0;
    font-family: "Pinyon Script", "Edwardian Script ITC", cursive;
    font-size: 60px;
    line-height: 1;
    color: var(--green);
    white-space: nowrap;
    transform: rotate(-6.5deg);
    transform-origin: 0 80%;
  }
  .programme {
    position: absolute;
    left: 741px;
    top: 657px;
    display: flex;
    align-items: center;
    gap: 10px;
  }
  .programme-square {
    width: 45px;
    height: 45px;
    background: var(--green-badge);
  }
  .programme-name {
    font-size: 19px;
    font-weight: 400;
    color: var(--ink-soft);
  }
</style>
</head>
<body>
  <main class="certificate">
    <svg class="compass-decoration" viewBox="0 0 954 737" role="img" aria-label="Faint green compass rose decoration">
      <defs>
        <radialGradient id="compassGlow" cx="50%" cy="50%" r="50%">
          <stop offset="0%" stop-color="var(--green-faint)" stop-opacity="0.9"/>
          <stop offset="70%" stop-color="var(--green-faint)" stop-opacity="0.6"/>
          <stop offset="100%" stop-color="var(--green-faint)" stop-opacity="0"/>
        </radialGradient>
      </defs>
      <ellipse cx="797" cy="307" rx="360" ry="290" fill="url(#compassGlow)"/>
    </svg>

    <svg class="swoosh" viewBox="0 0 954 737" aria-hidden="true">
      <path d="M0,695 C150,688 300,705 430,737 L0,737 Z" fill="var(--green-mid)"/>
      <path d="M954,420 C900,560 790,670 620,737 L954,737 Z" fill="var(--green-pale)"/>
      <path d="M954,285 C900,500 750,665 460,737 L620,737 C790,670 900,560 954,420 Z" fill="var(--green-mid)"/>
      <path d="M954,150 C890,420 700,640 300,737 L460,737 C750,665 900,500 954,285 Z" fill="var(--green-deep)"/>
    </svg>

    <h1 class="title">
      <span class="title-main">CERTIFICATE</span>
      <span class="title-sub">OF COMPLETION</span>
    </h1>

    <div class="brand">
      <div class="brand-square"></div>
      <div class="brand-name">
        <span>HOLLIS</span>
        <span>VAN TREEVE</span>
        <span class="brand-suffix">&amp; Associates</span>
      </div>
    </div>

    <section class="award">
      <p class="award-lead">This certificate is awarded to</p>
      <h2 class="recipient">MAYA CLARKE</h2>
      <p class="award-reason">For successfully completing and contributing to the three day<br>Bright Harbour programme.</p>
    </section>

    <div class="sign-field sign-date">Date</div>
    <div class="sign-field sign-signature">Signature</div>

    <p class="anniversary">25th year of existence</p>

    <div class="programme">
      <div class="programme-square"></div>
      <span class="programme-name">Bright Harbour</span>
    </div>
  </main>
</body>
</html>
```